8x8 Social Media Ad - Harbor Summit Expo

Attention Real Estate Agents
Please join us for our
Quarterly Real Estate Training Expo
The 2nd Saturday of February, May, August and November
Our Next Training Expo is _________________________________
From 9 am to 1 pm
at
Marlowe Suites Fernridge Station
4187 Copperleaf Lane, Greenbelt, MD 20770
Scheduled Speakers
9:00 am - Desmond Pryce - Orientation
9:30 am - Terrell Oakes - Multiple Income Streams / Keystone Track
10:00 am - Lorna Beckett - Marketing though Social Media
10:45 am - Raul Denning - Generating Business through Kelp-Nest
11:30 am - Tunde Adesemi - Real Estate Investing
12:15 pm - Marcus Oyelowo - (Main Speaker) Training Topic TBA
For more information call Desmond Pryce at (240) 555-0192 or email dpryce@harborsummithomes.example

```html
<!DOCTYPE html>
<html lang="en">
<head>
<meta charset="utf-8">
<title>Harbor Summit Expo – Quarterly Real Estate Training Expo</title>
<link rel="stylesheet" href="https://fonts.googleapis.com/css2?family=Montserrat:ital,wght@0,400;0,500;0,600;0,700;0,800;0,900;1,900&display=swap">
<style>
  :root{
    --navy-deep:#142d5e;
    --navy:#1f4585;
    --navy-mid:#25508f;
    --teal:#13959e;
    --teal-dark:#0d7b83;
    --yellow:#fff200;
    --orange:#f6a81c;
    --black:#121212;
    --white:#ffffff;
    --ink:#1a1a1a;
  }
  *{margin:0;padding:0;box-sizing:border-box}
  html,body{width:1200px;height:1200px;overflow:hidden;background:var(--navy-deep)}
  .ad{
    position:relative;width:1200px;height:1200px;overflow:hidden;
    font-family:"Montserrat",sans-serif;color:var(--white);
    background:radial-gradient(ellipse at 45% 40%, var(--navy-mid) 0%, var(--navy) 45%, var(--navy-deep) 100%);
  }
  .rule{position:absolute;left:0;width:1200px;height:5px;background:linear-gradient(90deg,transparent,var(--teal) 15%,var(--teal) 85%,transparent)}
  .rule--top{top:26px}
  .rule--bottom{top:1156px}
  .divider{position:absolute;left:607px;top:60px;width:1px;height:1080px;background:rgba(255,255,255,.18)}

  .attention{position:absolute;left:0;top:0}
  .attention svg{position:absolute;left:0;top:0}
  .attention__word{
    position:absolute;left:180px;top:116px;font-weight:900;font-style:italic;
    font-size:58px;letter-spacing:1px;color:var(--white);transform:rotate(-3deg);
    text-shadow:0 3px 0 rgba(0,0,0,.35);white-space:nowrap;
  }
  .audience{position:absolute;left:127px;top:240px;font-size:41px;font-weight:700;letter-spacing:.5px}

  .portrait{position:absolute;width:166px;height:166px;border-radius:50%;
    background:radial-gradient(circle at 50% 40%, #4a3a32 0%, #2d2a2e 55%, var(--teal) 56%, var(--teal-dark) 100%);
    box-shadow:4px 6px 10px rgba(0,0,0,.45)}
  .speaker-name{position:absolute;font-weight:700;font-size:27px;letter-spacing:1px;white-space:nowrap}

  .brand-band{position:absolute;left:0;top:917px;width:600px;height:191px;
    background:linear-gradient(90deg,var(--white) 0%,var(--white) 42%,rgba(255,255,255,.55) 75%,rgba(255,255,255,0) 100%)}
  .brand{position:absolute;left:78px;top:965px;display:flex;align-items:center;gap:16px}
  .brand__mark{width:54px;height:54px;background:var(--teal)}
  .brand__name{font-weight:700;font-size:26px;line-height:1.2;color:var(--teal)}

  .invite{position:absolute;left:645px;top:148px;font-weight:800;font-size:33px;color:var(--yellow);letter-spacing:.5px;white-space:nowrap}
  .headline{position:absolute;left:624px;font-weight:900;color:var(--white);line-height:1;letter-spacing:-1px;white-space:nowrap}
  .headline--q{top:203px;font-size:84px}
  .headline--r{top:290px;font-size:76px}
  .headline--t{top:360px;font-size:99px}
  .headline--e{top:444px;font-size:184px;letter-spacing:-4px}

  .schedule-bar{position:absolute;left:633px;top:630px;width:527px;height:56px;display:flex;border:2px solid var(--teal)}
  .schedule-bar__day{width:208px;background:var(--teal);display:flex;align-items:center;padding-left:10px;font-weight:800;font-size:44px;gap:12px}
  .schedule-bar__day sup{font-size:26px;vertical-align:20px}
  .schedule-bar__sep{width:2px;height:36px;background:var(--white)}
  .schedule-bar__months{flex:1;background:var(--white);color:var(--ink);display:flex;align-items:center;justify-content:center;font-size:25px;font-weight:500;letter-spacing:.5px;white-space:nowrap}

  .venue{position:absolute;left:640px;top:698px;font-size:19px;line-height:24px;letter-spacing:.4px;white-space:nowrap}
  .venue__next{position:absolute;left:638px;top:750px;font-size:19px;letter-spacing:.4px;white-space:nowrap}
  .blank{display:inline-block;width:82px;border-bottom:1px solid var(--white);margin:0 2px;vertical-align:-2px}

  .speakers-title{position:absolute;left:644px;top:790px;font-size:27px;font-weight:600;color:var(--teal);letter-spacing:.5px}
  .speakers{position:absolute;left:640px;top:831px;width:532px;border-collapse:collapse;border:1px solid rgba(255,255,255,.8);font-size:14px}
  .speakers td{height:21px;border-top:1px solid rgba(255,255,255,.8);white-space:nowrap;padding:0}
  .speakers .time{width:78px;font-weight:700;padding-left:2px}
  .speakers .who{width:164px;font-weight:700;text-align:right;padding-right:22px}
  .speakers .topic{font-weight:400;letter-spacing:.3px}

  .contact{position:absolute;left:633px;top:983px;font-size:22px;letter-spacing:.6px;white-space:nowrap}
  .phone{position:absolute;left:628px;top:1026px;font-size:67px;font-weight:800;color:var(--teal);letter-spacing:1px;white-space:nowrap}
  .email{position:absolute;left:636px;top:1098px;font-size:21px;letter-spacing:.2px;white-space:nowrap}
</style>
</head>
<body>
<main class="ad">
  <div class="rule rule--top"></div>
  <div class="rule rule--bottom"></div>
  <div class="divider"></div>

  <section class="attention">
    <svg width="610" height="270" viewBox="0 0 610 270" aria-hidden="true">
      <path d="M40 78 L170 73 L132 262 L12 264 Z" fill="var(--teal)"/>
      <path d="M158 82 L602 73 L586 222 L128 235 Z" fill="var(--orange)"/>
      <path d="M168 92 L590 86 L576 210 L142 222 Z" fill="var(--black)"/>
      <path d="M74 94 L102 92 L92 196 L70 198 Z" fill="#e8e8e8"/>
      <circle cx="80" cy="224" r="15" fill="#e8e8e8"/>
    </svg>
    <div class="attention__word">ATTENTION</div>
  </section>
  <div class="audience">Real Estate Agents</div>

  <div class="portrait" style="left:114px;top:394px" role="img" aria-label="Portrait photo of speaker Reggie"></div>
  <div class="portrait" style="left:296px;top:394px" role="img" aria-label="Portrait photo of speaker Raul"></div>
  <div class="portrait" style="left:36px;top:654px" role="img" aria-label="Portrait photo of speaker Desmond"></div>
  <div class="portrait" style="left:214px;top:654px" role="img" aria-label="Portrait photo of speaker Marcus"></div>
  <div class="portrait" style="left:395px;top:654px" role="img" aria-label="Portrait photo of speaker Tunde"></div>

  <div class="speaker-name" style="left:150px;top:568px">REGGIE</div>
  <div class="speaker-name" style="left:348px;top:566px">RAUL</div>
  <div class="speaker-name" style="left:30px;top:828px">DESMOND</div>
  <div class="speaker-name" style="left:238px;top:828px">MARCUS</div>
  <div class="speaker-name" style="left:440px;top:828px">TUNDE</div>

  <div class="brand-band"></div>
  <div class="brand">
    <div class="brand__mark"></div>
    <div class="brand__name">HARBOR SUMMIT<br>REALTY GROUP</div>
  </div>

  <div class="invite">PLEASE JOIN US FOR OUR</div>
  <h1>
    <span class="headline headline--q">QUARTERLY</span>
    <span class="headline headline--r">REAL ESTATE</span>
    <span class="headline headline--t">TRAINING</span>
    <span class="headline headline--e">EXPO</span>
  </h1>

  <div class="schedule-bar">
    <div class="schedule-bar__day"><span>2<sup>nd</sup></span><span class="schedule-bar__sep"></span><span>SAT</span></div>
    <div class="schedule-bar__months">FEB | MAY | AUG | NOV</div>
  </div>

  <div class="venue">Marlowe Suites Fernridge Station<br>4187 Copperleaf Lane, Greenbelt, MD 20770</div>
  <div class="venue__next">Our Next Training Expo is <span class="blank"></span>-From 9 am to 1 pm</div>

  <div class="speakers-title">Scheduled Speakers</div>
  <table class="speakers">
    <tr><td class="time">9:00 AM</td><td class="who">Desmond Pryce</td><td class="topic">Orientation</td></tr>
    <tr><td class="time">9:30 AM</td><td class="who">Terrell Oakes</td><td class="topic">Multiple Income Streams / Keystone Track</td></tr>
    <tr><td class="time">10:00 AM</td><td class="who">Lorna Beckett</td><td class="topic">Marketing though Social Media</td></tr>
    <tr><td class="time">10:45 AM</td><td class="who">Raul Denning</td><td class="topic">Generating Business through Kelp-Nest</td></tr>
    <tr><td class="time">11:30 AM</td><td class="who">Tunde Adesemi</td><td class="topic">Real Estate Investing</td></tr>
    <tr><td class="time">12:15 PM</td><td class="who">Marcus Oyelowo</td><td class="topic">(Main Speaker) Training Topic TBA</td></tr>
  </table>

  <div class="contact">For more information call Desmond Pryce at</div>
  <div class="phone">(240) 555-0192</div>
  <div class="email">or email dpryce@harborsummithomes.example</div>
</main>
</body>
</html>
```